Seven Rising Steps - Site signage graphic

I need a large board creating to show our Seven Bright Paths plan.

I have added a previous version of this called Seven Bold Moves as well as the draft (AI) version of Seven Rising Steps and our new PowerPoint as an example of branding .

Target Market(s)

Colleagues and visitors to site

Industry/Entity Type

Food manufacturing

Font styles to use
Other font styles liked:
• Raleway Medium

Requirements
Must have
• Clear and all text as per AI mock up

```html
<!DOCTYPE html>
<html lang="en">
<head>
<meta charset="utf-8">
<title>Seven Bright Paths – Site Board</title>
<link href="https://fonts.googleapis.com/css2?family=Bebas+Neue&family=Montserrat:ital,wght@0,500;0,700;0,800;1,700;1,800&family=Kalam:wght@700&display=swap" rel="stylesheet">
<style>
:root{
  --green-deep:#063d24;
  --green:#0b4a2c;
  --green-text:#0d4a2a;
  --yellow:#f5b82a;
  --orange:#e8781e;
  --panel:#ececeb;
  --ink:#1d1d1d;
  --tab1:#8c9b3d;--tab1d:#6c7a2a;
  --tab2:#e5ab1f;--tab2d:#c48a10;
  --tab3:#c57a23;--tab3d:#9d5b14;
  --tab4:#b9291f;--tab4d:#8e1a13;
  --tab5:#7b1c15;--tab5d:#5a110c;
}
*{box-sizing:border-box;margin:0;padding:0}
html,body{width:1200px;height:1090px;overflow:hidden;background:#fff}
.board{position:absolute;left:0;top:81px;width:1200px;height:928px;background:var(--panel)}
.intro{position:absolute;left:0;top:0;width:432px;height:808px;background:linear-gradient(180deg,#0b4a2c 0%,#0a5030 55%,#0c4d2c 100%);overflow:hidden}
.kicker{position:absolute;left:64px;top:62px;font:800 21px/25px Montserrat,sans-serif;color:#fff;text-transform:uppercase}
.kicker span{color:var(--yellow)}
.headline{position:absolute;left:62px;top:160px;width:320px;font-family:"Bebas Neue",sans-serif;font-weight:400}
.headline .top{display:flex;align-items:center;gap:14px;height:52px;color:#fff;font-size:58px;line-height:52px}
.headline .top::after{content:"";flex:1;height:1.5px;background:var(--yellow)}
.headline .big{display:block;height:80px;color:var(--yellow);font-size:94px;line-height:84px;letter-spacing:.5px}
.tagline{position:absolute;left:64px;top:398px;font:italic 700 19px/25px Montserrat,sans-serif;color:#fff}
.tagline span{color:var(--yellow)}
.farm-photo{position:absolute;left:0;top:500px;width:432px;height:308px;background:linear-gradient(180deg,#2f5a3a 0%,#9fb0a8 12%,#6d8a4a 28%,#4f7a2c 55%,#3c5e22 80%,#5a6e2a 100%)}
.priorities{position:absolute;left:432px;top:44px;width:768px}
.priority{position:relative;height:150px;border-bottom:1px solid #dcdcdb;box-shadow:0 3px 4px -3px rgba(0,0,0,.12)}
.priority:last-child{border-bottom:none;box-shadow:none}
.tab{position:absolute;left:0;top:12px;width:120px;height:114px}
.tab-num{position:absolute;left:0;top:12px;width:106px;height:114px;display:flex;align-items:center;justify-content:center;font:72px/1 "Bebas Neue",sans-serif;color:#fff}
.badge{position:absolute;left:149px;top:12px;width:68px;height:68px;border-radius:50%;background:#fff;box-shadow:0 3px 6px rgba(0,0,0,.25);display:flex;align-items:center;justify-content:center}
.badge-core{width:56px;height:56px;border-radius:50%;display:flex;align-items:center;justify-content:center}
.copy{position:absolute;left:236px;top:8px;width:480px}
.copy h2{font:400 34px/1 "Bebas Neue",sans-serif;color:var(--green-text);letter-spacing:.2px}
.copy h3{margin-top:4px;font:400 20px/1 "Bebas Neue",sans-serif;color:var(--green-text);padding-bottom:8px;position:relative}
.copy h3 em{font-style:normal;color:var(--orange)}
.copy h3::after{content:"";position:absolute;left:0;bottom:0;width:120px;height:1.5px;background:var(--orange)}
.copy p{margin-top:10px;font:500 11.4px/15px Montserrat,sans-serif;color:var(--ink);width:470px}
.footer{position:absolute;left:0;top:808px;width:1200px;height:120px;background:linear-gradient(90deg,var(--green-deep),#0a4a2b 50%,var(--green-deep));display:flex;align-items:center}
.footer-lead{margin-left:64px;font:italic 800 16px/23px Montserrat,sans-serif;color:#fff;text-transform:uppercase;white-space:nowrap}
.footer-lead span{color:var(--yellow)}
.divider{width:2px;height:40px;background:var(--yellow);margin:0 28px;flex:none}
.motto{font:400 41px/1 "Bebas Neue",sans-serif;color:#fff;letter-spacing:.3px;white-space:nowrap}
.motto .y{color:var(--yellow)}.motto .o{color:var(--orange)}
.signoff{font:700 18px/19px Kalam,sans-serif;color:#fff;text-transform:uppercase;transform:rotate(-4deg);white-space:nowrap}
.signoff span{color:var(--yellow);display:block}
</style>
</head>
<body>
<div class="board">
  <section class="intro">
    <p class="kicker">From<br>Cheesemakers<br><span>To</span> Changemakers</p>
    <h1 class="headline">
      <span class="top">Seven</span>
      <span class="big">Bright</span>
      <span class="big">Paths</span>
    </h1>
    <p class="tagline">Proud of our heritage.<br><span>Focused on our future.</span></p>
    <div class="farm-photo" role="img" aria-label="Photograph of a red barn with silos in green farmland, wooden fence and hills behind"></div>
  </section>

  <section class="priorities">
    <article class="priority">
      <svg class="tab" viewBox="0 0 120 114"><polygon points="0,0 88,0 120,57 88,114 0,114" fill="var(--tab1d)"/><polygon points="0,0 82,0 106,57 82,114 0,114" fill="var(--tab1)"/></svg>
      <div class="tab-num">01</div>
      <div class="badge"><div class="badge-core" style="background:var(--tab1)">
        <svg width="34" height="26" viewBox="0 0 34 26" fill="#fff"><circle cx="17" cy="7" r="5"/><circle cx="7" cy="9" r="3.5"/><circle cx="27" cy="9" r="3.5"/><path d="M8 24c0-6 4-10 9-10s9 4 9 10z"/><path d="M0 23c0-4 3-8 7-8 2 0 3 .5 4 1.5-2 2-3 4-3 6.5z"/><path d="M34 23c0-4-3-8-7-8-2 0-3 .5-4 1.5 2 2 3 4 3 6.5z"/></svg>
      </div></div>
      <div class="copy">
        <h2>People, Places &amp; Products</h2>
        <h3>We do things <em>the right way</em></h3>
        <p>Our success starts with great people, strong communities and quality milk. We are committed to producing food responsibly, supporting our farming partners and creating opportunities for future generations.</p>
      </div>
    </article>

    <article class="priority">
      <svg class="tab" viewBox="0 0 120 114"><polygon points="0,0 88,0 120,57 88,114 0,114" fill="var(--tab2d)"/><polygon points="0,0 82,0 106,57 82,114 0,114" fill="var(--tab2)"/></svg>
      <div class="tab-num">02</div>
      <div class="badge"><div class="badge-core" style="background:var(--tab2)">
        <svg width="30" height="32" viewBox="0 0 30 32" fill="none" stroke="#fff" stroke-width="2"><path d="M15 2l11 4v9c0 8-5 13-11 15C9 28 4 23 4 15V6z"/><rect x="10.5" y="14" width="9" height="7" fill="#fff"/><path d="M12 14v-3a3 3 0 016 0v3"/></svg>
      </div></div>
      <div class="copy">
        <h2>Cyber Security</h2>
        <h3>Protecting <em>what matters</em></h3>
        <p>Every colleague plays a role in keeping our information, systems and customers safe. Strong cyber security protects our business today and supports our future growth.</p>
      </div>
    </article>

    <article class="priority">
      <svg class="tab" viewBox="0 0 120 114"><polygon points="0,0 88,0 120,57 88,114 0,114" fill="var(--tab3d)"/><polygon points="0,0 82,0 106,57 82,114 0,114" fill="var(--tab3)"/></svg>
      <div class="tab-num">03</div>
      <div class="badge"><div class="badge-core" style="background:var(--tab3)">
        <svg width="30" height="34" viewBox="0 0 30 34" fill="#fff"><path d="M8 20l-5 11 5-1 3 4 4-9zM22 20l5 11-5-1-3 4-4-9z"/><circle cx="15" cy="13" r="11"/><circle cx="15" cy="13" r="7.5" fill="var(--tab3)"/><path d="M15 8.5l1.4 3 3.2.3-2.4 2.1.7 3.1-2.9-1.7-2.9 1.7.7-3.1-2.4-2.1 3.2-.3z"/></svg>
      </div></div>
      <div class="copy">
        <h2>Quality &amp; Continuous Improvement</h2>
        <h3>Be the best at <em>what we do</em></h3>
        <p>Quality and food safety are at the heart of everything we do. By continually improving our processes, reducing waste and learning every day, we deliver products our customers can trust.</p>
      </div>
    </article>

    <article class="priority">
      <svg class="tab" viewBox="0 0 120 114"><polygon points="0,0 88,0 120,57 88,114 0,114" fill="var(--tab4d)"/><polygon points="0,0 82,0 106,57 82,114 0,114" fill="var(--tab4)"/></svg>
      <div class="tab-num">04</div>
      <div class="badge"><div class="badge-core" style="background:var(--tab4)">
        <svg width="32" height="30" viewBox="0 0 32 30" fill="#fff"><path d="M8 2l1 2 2 .3-1.5 1.4.4 2.1L8 6.8 6.1 7.8l.4-2.1L5 4.3 7 4zM16 0l1 2 2 .3-1.5 1.4.4 2.1L16 4.8l-1.9 1 .4-2.1L13 2.3 15 2zM24 2l1 2 2 .3-1.5 1.4.4 2.1-1.9-1-1.9 1 .4-2.1L21 4.3 23 4z"/><circle cx="16" cy="14" r="4"/><circle cx="7" cy="16" r="3.2"/><circle cx="25" cy="16" r="3.2"/><path d="M9 29c0-6 3-9 7-9s7 3 7 9z"/><path d="M1 28c0-4 2-7 6-7 1.5 0 2.5.4 3.3 1-1.4 1.6-2.3 3.6-2.3 6z"/><path d="M31 28c0-4-2-7-6-7-1.5 0-2.5.4-3.3 1 1.4 1.6 2.3 3.6 2.3 6z"/></svg>
      </div></div>
      <div class="copy">
        <h2>Customer Focus</h2>
        <h3>Build <em>trust.</em> Create <em>value.</em> For the <em>long term.</em></h3>
        <p>We build strong, long-term relationships based on trust by understanding our customers’ needs and working together to deliver outstanding value.</p>
      </div>
    </article>

    <article class="priority">
      <svg class="tab" viewBox="0 0 120 114"><polygon points="0,0 88,0 120,57 88,114 0,114" fill="var(--tab5d)"/><polygon points="0,0 82,0 106,57 82,114 0,114" fill="var(--tab5)"/></svg>
      <div class="tab-num">05</div>
      <div class="badge"><div class="badge-core" style="background:var(--tab5)">
        <svg width="30" height="34" viewBox="0 0 30 34" fill="none" stroke="#fff" stroke-width="2"><path d="M15 6a9 9 0 00-5 16.5V26h10v-3.5A9 9 0 0015 6z" fill="#fff"/><path d="M11 29h8M12 32h6"/><path d="M15 0v3M3 5l2 2M27 5l-2 2M0 15h3M27 15h3"/><path d="M12 14l3 3 3-3M15 17v5" stroke="var(--tab5)"/></svg>
      </div></div>
      <div class="copy">
        <h2>Transformation &amp; Innovation</h2>
        <h3>Shaping <em>tomorrow today</em></h3>
        <p>We challenge ourselves to think differently, embrace change and never stand still. Through innovation, collaboration and continuous improvement, we will build a stronger, smarter and more sustainable Marrow Dale Foods for the future.</p>
      </div>
    </article>
  </section>

  <footer class="footer">
    <p class="footer-lead">From farm to fork.<br><span>We’re shaping the industry.</span></p>
    <span class="divider"></span>
    <p class="motto">One <span class="y">business.</span> One <span class="o">purpose.</span> Bright <span class="y">paths.</span></p>
    <span class="divider"></span>
    <p class="signoff">Let’s thrive<span>together.</span></p>
  </footer>
</div>
</body>
</html>
```